Short term vacation rental

I need a simple site the we can rent a duplex that is on the sand in Indian rocks beach Fl needs to be able to sync with multiple calendars like staylumo.com qelt tovn using Wordpress

```html
<!DOCTYPE html>
<html lang="en">
<head>
<meta charset="utf-8">
<title>Saltwind Retreats – Indian Rocks Beach Duplex</title>
<link href="https://fonts.googleapis.com/css2?family=Cinzel:wght@400;500;600&family=Poppins:wght@400;500;600&display=swap" rel="stylesheet">
<style>
:root{
  --navy:#1b2d5e;
  --teal:#9cbfc1;
  --teal-text:#8fb4b8;
  --ink:#222;
  --white:#fff;
  --line:#d6d6d6;
}
*{box-sizing:border-box;margin:0;padding:0}
html,body{width:1200px;height:5181px;overflow:hidden}
body{font-family:"Poppins",sans-serif;color:var(--ink);background:var(--white);position:relative}
.abs{position:absolute}
.btn{display:inline-block;background:var(--navy);color:var(--white);font:500 12px "Poppins",sans-serif;letter-spacing:.5px;text-transform:uppercase;padding:12px 26px}

/* hero */
.hero{position:absolute;left:0;top:0;width:1200px;height:900px;
  background:linear-gradient(180deg,#e9ecef 0%,#eee8d6 25%,#f4d78a 40%,#f2b84a 47%,#c98b3e 50%,#4b5366 56%,#2d3a4c 70%,#6b6358 85%,#8a7865 100%)}
.logo{position:absolute;display:flex;align-items:center;gap:10px;font:500 30px "Cinzel",serif;color:var(--navy);letter-spacing:1px}
.logo .dot{width:14px;height:14px;border-radius:50%;background:var(--teal)}
.nav{position:absolute;left:513px;top:70px;display:flex;gap:18px;font:500 13px "Poppins",sans-serif;color:var(--ink);text-transform:uppercase}
.hero .book{position:absolute;left:925px;top:60px;padding:11px 24px;font-size:12px}
.hero h1{position:absolute;left:140px;top:212px;font:500 44px/53px "Cinzel",serif;color:var(--navy);text-transform:uppercase}
.hero h1 .dark{color:#111}
.hero .lede{position:absolute;left:140px;top:398px;font:500 13.5px/23px "Poppins",sans-serif;color:#111;width:400px}
.play{position:absolute;left:818px;top:328px;width:80px;height:80px}

/* booking */
.booking{position:absolute;left:136px;top:804px;width:946px;height:222px;background:var(--teal)}
.booking .field{position:absolute;top:52px}
.booking label{display:block;font:500 11px "Poppins",sans-serif;color:var(--white);margin-bottom:14px}
.booking .box{background:var(--white);height:36px;font:400 11px "Poppins",sans-serif;color:#555;display:flex;align-items:center;justify-content:space-between;padding:0 14px}
.booking .search{position:absolute;left:836px;top:88px;width:46px;height:36px}
.booking .channels{position:absolute;left:0;width:100%;top:160px;text-align:center;font:400 12px "Poppins",sans-serif;color:var(--navy)}

/* about */
.about-photo{position:absolute;left:136px;top:1183px;width:418px;height:418px;border-radius:50%;
  background:linear-gradient(135deg,#dfe3e6,#9ea7ad 55%,#5b5148)}
.section-title{font:500 38px/46px "Cinzel",serif;text-transform:uppercase}
.section-title .soft{color:var(--teal-text)}
.section-title .strong{color:#111}
.about .section-title{position:absolute;left:628px;top:1140px}
.rule{position:absolute;height:3px;width:100px;background:var(--navy)}
.about p{position:absolute;left:628px;width:428px;font:400 12.4px/22px "Poppins",sans-serif;color:#333;text-align:justify}

/* why */
.why .section-title{position:absolute;left:0;width:1200px;top:1765px;text-align:center}
.feature{position:absolute;top:1887px;width:270px;height:346px;text-align:center}
.feature.active{background:linear-gradient(180deg,#f4f4f4,#e6e6e6);border:1px solid #d2d2d2}
.feature .icon{width:70px;height:70px;border-radius:50%;background:var(--teal);margin:50px auto 22px;display:flex;align-items:center;justify-content:center}
.feature h3{font:500 15.5px "Poppins",sans-serif;color:#111;margin-bottom:18px}
.feature p{font:400 12.4px/24px "Poppins",sans-serif;color:#444;width:220px;margin:0 auto}

/* amenities */
.amenities{position:absolute;left:0;top:2396px;width:1200px;height:830px;background:linear-gradient(90deg,var(--navy) 50%,var(--teal) 50%)}
.amenities .section-title{position:absolute;left:0;width:1200px;top:120px;text-align:center;color:var(--white)}
.amenities h4{position:absolute;top:260px;font:600 17px "Poppins",sans-serif;color:var(--white);text-transform:uppercase}
.amenities ul{position:absolute;top:330px;list-style:none;width:440px}
.amenities li{position:relative;padding-left:28px;margin-bottom:26px;font:400 12px/26px "Poppins",sans-serif}
.amenities li::before{content:"";position:absolute;left:0;top:9px;width:10px;height:10px;border-radius:50%}
.room li{color:var(--white)}
.room li::before{background:var(--teal)}
.prop li{color:var(--navy)}
.prop li span{color:var(--white)}
.prop li::before{background:var(--navy)}
.amenities .outline{position:absolute;left:529px;top:702px;border:1px solid var(--white);background:transparent;padding:10px 24px}

/* gallery */
.gallery .section-title{position:absolute;left:0;width:1200px;top:3348px;text-align:center}
.shot{position:absolute}

/* location */
.location{position:absolute;left:0;top:4155px;width:1200px;height:585px;background:#5ec3e0}
.map{position:absolute;left:672px;top:0;width:528px;height:585px;background:linear-gradient(160deg,#b9dcb0,#9fd0a2 50%,#7cc3d4)}
.card{position:absolute;left:145px;top:173px;width:297px;height:244px;background:var(--white)}
.card .row{position:absolute;left:28px;display:flex;gap:18px}
.card .pin{width:50px;height:50px;flex:none}
.card small{display:block;font:500 12px "Poppins",sans-serif;color:var(--teal-text);margin-bottom:6px}
.card b{font:500 12.5px/22px "Poppins",sans-serif;color:#111;text-transform:uppercase}

/* footer */
.footer .logo{left:0;width:1200px;justify-content:center;top:4872px;font-size:34px}
.footer .nav{left:260px;top:4975px;font-size:13px}
.footer .btn{position:absolute;left:674px;top:4962px;padding:11px 26px}
.social{position:absolute;top:4963px;display:flex;gap:8px;left:816px}
.social span{width:34px;height:34px;border-radius:50%;background:var(--teal)}
.footer hr{position:absolute;left:195px;top:5025px;width:814px;border:0;border-top:1px solid var(--line)}
.footer .copy{position:absolute;left:0;width:1200px;top:5057px;text-align:center;font:400 12.5px "Poppins",sans-serif;color:#222}
</style>
</head>
<body>

<section class="hero" role="img" aria-label="Sunset over the Gulf with two people in beach chairs on the sand">
  <div class="logo" style="left:140px;top:70px"><span class="dot"></span>Saltwind Retreats</div>
  <nav class="nav"><span>Home</span><span>About Us</span><span>Units &amp; Availability</span><span>Contact</span></nav>
  <a class="btn book">Book Now</a>
  <h1><span>Indian Rocks Beach</span><br><span class="dark">Duplex Steps From<br>The Sand</span></h1>
  <p class="lede">Wake up to the sound of the waves and step directly onto the pristine sands of Indian Rocks Beach.</p>
  <svg class="play" viewBox="0 0 80 80"><circle cx="40" cy="40" r="40" fill="#9cbfc1"/><path d="M34 30 L50 40 L34 50Z" fill="#fff"/></svg>
</section>

<form class="booking">
  <div class="field" style="left:44px;width:162px"><label>Check In Date</label><div class="box">DD/MM/YYYY <span>▦</span></div></div>
  <div class="field" style="left:220px;width:162px"><label>Check Out Date</label><div class="box">DD/MM/YYYY <span>▦</span></div></div>
  <div class="field" style="left:396px;width:162px"><label>Guests</label><div class="box">2 Guests <span>⌄</span></div></div>
  <div class="field" style="left:570px;width:250px"><label>Property Type</label><div class="box">Duplex (Sand Right) <span>⌄</span></div></div>
  <svg class="search" viewBox="0 0 46 36"><rect width="46" height="36" fill="#1b2d5e"/><circle cx="22" cy="17" r="5" fill="none" stroke="#fff" stroke-width="2"/><path d="M26 21l4 4" stroke="#fff" stroke-width="2"/></svg>
  <p class="channels">with staylumo.com • qelt • tovn • Voyara • Harbrook</p>
</form>

<section class="about">
  <div class="about-photo" role="img" aria-label="Bright living room of the duplex with sofa, armchair and coffee table"></div>
  <h2 class="section-title"><span class="soft">The Heart Behind</span><br><span class="strong">Saltwind Inn</span></h2>
  <div class="rule" style="left:628px;top:1250px"></div>
  <p style="top:1285px">At the helm of the Saltwind Inn is Marla Dennet, a passionate and dedicated owner who treats every guest as part of her extended family. Her deep love for the inn and commitment to its role in the Indian Rocks Beach community shines through in every detail.</p>
  <p style="top:1400px">Marla's hands-on approach ensures each stay is filled with warmth, care, and the unique charm that has made Saltwind Inn a beloved retreat since she purchased it in 2015. Under her stewardship, the inn continues to be a vital piece of the community, creating unforgettable memories for guests while contributing to the vibrant spirit of Indian Rocks Beach.</p>
  <a class="btn abs" style="left:628px;top:1570px">Learn More</a>
</section>

<section class="why">
  <h2 class="section-title"><span class="soft">Why</span> <span class="strong">Choose Us</span></h2>
  <div class="rule" style="left:550px;top:1832px"></div>
  <div class="feature" style="left:152px">
    <div class="icon"><svg width="40" height="30" viewBox="0 0 40 30"><path d="M2 12q6-6 12 0t12 0 12 0M2 20q6-6 12 0t12 0 12 0M2 28q6-6 12 0t12 0 12 0" fill="none" stroke="#fff" stroke-width="2"/></svg></div>
    <h3>Steps from the Beach</h3><p>Feel the soft sand between your toes within moments of leaving your room.</p>
  </div>
  <div class="feature active" style="left:471px">
    <div class="icon"><svg width="44" height="36" viewBox="0 0 44 36"><circle cx="22" cy="18" r="12" fill="none" stroke="#fff" stroke-width="2"/><circle cx="22" cy="18" r="7" fill="none" stroke="#fff" stroke-width="2"/><path d="M4 4v28M40 4v28" stroke="#fff" stroke-width="2"/></svg></div>
    <h3>Walkable Dining</h3><p>Pelicove Grill: Famous for fresh local seafood and outdoor patio dining.</p>
  </div>
  <div class="feature" style="left:778px">
    <div class="icon"><svg width="30" height="36" viewBox="0 0 30 36"><rect x="3" y="2" width="24" height="32" fill="none" stroke="#fff" stroke-width="2"/><path d="M8 10h14M8 16h14M8 22h10" stroke="#fff" stroke-width="2"/></svg></div>
    <h3>No Extra Fees</h3><p>Every rupee goes directly toward your stay, not to a tech corporation.</p>
  </div>
</section>

<section class="amenities">
  <h2 class="section-title">Our Amenities</h2>
  <div class="rule" style="left:550px;top:190px;width:98px;background:#fff;height:2px"></div>
  <h4 style="left:142px">Room Amenities</h4>
  <ul class="room" style="left:142px">
    <li>Full Kitchen:<br>Fully equipped kitchen for cooking your own meals.</li>
    <li>Dining Area:<br>Dedicated space to enjoy family meals.</li>
    <li>Flat-Screen TVs:<br>Available in both bedrooms and living areas.</li>
    <li>Climate Control:<br>Central air conditioning and heating for ultimate comfort.</li>
  </ul>
  <h4 style="left:661px">Property &amp; Location Amenities</h4>
  <ul class="prop" style="left:661px">
    <li>Steps to the Beach:<br><span>Quick and direct access to the shoreline.</span></li>
    <li>Water Sports &amp; Activities:<br><span>Perfect spot for surfing, paddleboarding, and fishing.</span></li>
    <li>Unforgettable Sunsets:<br><span>Ideal vantage point to watch spectacular evening views.</span></li>
    <li>Walkable Location:<br><span>Walking distance to local restaurants, parks, walking trails, and shops.</span></li>
  </ul>
  <a class="btn outline">Learn More</a>
</section>

<section class="gallery">
  <h2 class="section-title"><span class="soft">Our</span> <span class="strong">Gallery</span></h2>
  <div class="rule" style="left:550px;top:3413px"></div>
  <div class="shot" style="left:144px;top:3468px;width:216px;height:226px;background:linear-gradient(160deg,#b8d3e6,#c9b8a0 55%,#8f9a78)" role="img" aria-label="Aerial view of the beach duplex and neighbouring homes"></div>
  <div class="shot" style="left:376px;top:3468px;width:370px;height:226px;background:linear-gradient(180deg,#7fb6e6,#6fae9a 50%,#4e8a4c)" role="img" aria-label="Teal cottage entrance with palm trees and flower bushes"></div>
  <div class="shot" style="left:762px;top:3468px;width:294px;height:226px;background:linear-gradient(180deg,#5da5e8,#7cae7a 55%,#d8cdb2)" role="img" aria-label="Sandy boardwalk path leading to the beach"></div>
  <div class="shot" style="left:144px;top:3710px;width:368px;height:230px;background:linear-gradient(180deg,#cfe2ec,#b8894e 55%,#6b4b2c)" role="img" aria-label="Thatched beach bar under palm trees"></div>
  <div class="shot" style="left:528px;top:3710px;width:296px;height:230px;background:linear-gradient(160deg,#7fb4e0,#37b7c2 50%,#e6dcc4)" role="img" aria-label="Turquoise water meeting white sand from above"></div>
  <div class="shot" style="left:838px;top:3710px;width:218px;height:230px;background:linear-gradient(180deg,#6a7180,#d99a4f 45%,#3c3e44)" role="img" aria-label="Sunset over the Gulf seen from the shore"></div>
  <a class="btn abs" style="left:530px;top:3980px">Explore More</a>
</section>

<section class="location">
  <div class="map" role="img" aria-label="Map of Florida with a marker at Indian Rocks Beach"></div>
  <div class="card">
    <div class="row" style="top:40px">
      <svg class="pin" viewBox="0 0 50 50"><circle cx="25" cy="25" r="25" fill="#1b2d5e"/><path d="M25 14a7 7 0 0 0-7 7c0 6 7 14 7 14s7-8 7-14a7 7 0 0 0-7-7z" fill="#fff"/><circle cx="25" cy="21" r="2.5" fill="#1b2d5e"/></svg>
      <div><small>Location</small><b>1450 Shoreline Blvd.<br>Indian Rocks Beach,<br>Florida 33785</b></div>
    </div>
    <div style="position:absolute;left:0;top:140px;width:297px;border-top:1px solid #ddd"></div>
    <div class="row" style="top:165px">
      <svg class="pin" viewBox="0 0 50 50"><circle cx="25" cy="25" r="25" fill="#1b2d5e"/><path d="M19 15l4 0 2 6-3 2c1 3 3 5 6 6l2-3 6 2 0 4c-10 1-18-7-17-17z" fill="#fff"/></svg>
      <div><small>Phone</small><b>727-555-0148</b></div>
    </div>
  </div>
</section>

<footer class="footer">
  <div class="logo"><span class="dot"></span>Saltwind Retreats</div>
  <nav class="nav"><span>Home</span><span>About Us</span><span>Units &amp; Availability</span><span>Contact</span></nav>
  <a class="btn">Book Now</a>
  <div class="social"><span></span><span></span><span></span></div>
  <hr>
  <p class="copy">Copyright@2026.All Rights Reserved.</p>
</footer>

</body>
</html>
```